Website Design for a New Business Sharing Application

Purpose: Website for a new product – a sharing application called "Pondly.io"

Product concept: Easy sharing of business information. The application has different sections: tasks, calendars, documents, contacts, notes and links. The key feature of the application is that you can drag and drop information from different sections into a "share." A share is a page which lists all the types of information that you drag into it. You can add people to this "share."

Note: The application itself is not part of this project, just the website.

Website details: The site, in addition to being informational, will actually be the first point of entry for visitors into the application itself. Because of that, we would like the website design to reflect the look of the application, to create a smooth and seamless experience for the user moving from the website into the application (tough the website does not need to look *exactly* like the application). Included Product Tour screenshots show you the look of the application.

Website pages to be created: 4 pages
We are flexible in terms of the exact structure and placement of elements. You may change that any way you like. The pages are as follows:

Home page
Product Tour page
Press page
Blog page

Specific description of pages are provided in project files we will upload. We will also upload the logo, home page layout we have in mind, and other supporting files.

NOTE: Please submit first the design of the home page. Based on this design we will ask selected designers to submit designs for the other pages.

Target Market(s)

Business people who want to share work related files with their colleagues

Industry/Entity Type

Business

Requirements
Must have
• All the required features are listed in the description of the website and specific pages that we will upload.

```html
<!DOCTYPE html>
<html lang="en">
<head>
<meta charset="utf-8">
<title>Pondly.io — Share NOW</title>
<link rel="stylesheet" href="https://fonts.googleapis.com/css2?family=Barlow:wght@400;500;600;700&display=swap">
<style>
  :root {
    --page-bg: #ececec;
    --column-bg: #f5f5f5;
    --brand-blue: #2b7fc1;
    --brand-orange: #e0702a;
    --text-grey: #7a7a7a;
    --text-dark: #555555;
    --access-yellow: #f3d57a;
    --access-text: #8c7a46;
    --share-top: #8bc9ec;
    --share-bottom: #6aafdc;
    --tab-grey: #cfcfcf;
    --drop-red: #c9605a;
    --drop-plus: #f2d35a;
    --signup-purple: #8f70be;
    --signup-arrow: #b7a2dc;
    --footer-bg: #e5e5e5;
    --pricing-red: #d2304a;
    --c-files: #5ea9dc;
    --c-pictures: #8a55b5;
    --c-tasks: #b03a3a;
    --c-todos: #d8b24c;
    --c-calendars: #b443b8;
    --c-notes: #2e6db4;
    --c-links: #7fb04a;
  }
  * { box-sizing: border-box; margin: 0; padding: 0; }
  html, body { width: 1200px; height: 700px; overflow: hidden; }
  body {
    background: var(--page-bg);
    font-family: "Barlow", Arial, sans-serif;
    position: relative;
  }
  .column {
    position: absolute; left: 70px; top: 0; width: 1050px; height: 700px;
    background: var(--column-bg);
  }
  .brand {
    position: absolute; left: 450px; top: 50px; height: 70px;
    display: flex; align-items: center; gap: 16px;
  }
  .brand-dot { width: 54px; height: 54px; border-radius: 50%; background: var(--brand-blue); }
  .brand-name { font-size: 56px; font-weight: 600; color: var(--brand-blue); letter-spacing: -0.5px; }
  .access-button {
    position: absolute; left: 897px; top: 39px; width: 178px; height: 35px;
    background: var(--access-yellow); border-radius: 3px;
    color: var(--access-text); font-size: 18px; line-height: 35px; text-align: center;
  }
  .share-now {
    position: absolute; left: 344px; top: 178px; width: 512px; height: 127px;
    background: linear-gradient(var(--share-top), var(--share-bottom));
    border: 1px solid #6aa9d4; border-radius: 2px;
    color: #fff; font-size: 84px; font-weight: 700; text-align: center; line-height: 122px;
  }
  .feature-tab {
    position: absolute; left: 919px; width: 201px; background: var(--tab-grey);
    color: var(--text-grey); font-size: 17px; line-height: 20px; padding: 4px 14px;
  }
  .tab-fastest { top: 181px; height: 49px; }
  .tab-social { top: 242px; height: 28px; }
  .tagline {
    position: absolute; left: 0; top: 330px; width: 1200px; text-align: center;
    font-size: 37px; font-weight: 700; color: var(--text-grey);
  }
  .categories {
    position: absolute; left: 0; top: 394px; width: 1200px; text-align: center;
    font-size: 22px; letter-spacing: 0.3px;
  }
  .categories .sep { color: var(--text-grey); margin: 0 4px; }
  .drop-zone {
    position: absolute; left: 201px; top: 449px; width: 327px; height: 81px;
    background: var(--drop-red); border-radius: 2px; color: #fff;
    display: flex; align-items: center; gap: 24px; padding-left: 14px;
    font-size: 25px; line-height: 31px;
  }
  .or-label {
    position: absolute; left: 560px; top: 468px; width: 80px; text-align: center;
    font-size: 36px; font-weight: 700; color: var(--text-grey);
  }
  .signup {
    position: absolute; left: 676px; top: 449px; width: 327px; height: 81px;
    background: var(--signup-purple); border-radius: 2px; color: #fff;
  }
  .signup svg.envelope { position: absolute; left: 15px; top: 22px; }
  .signup-label { position: absolute; left: 70px; top: 4px; font-size: 13px; }
  .signup-input {
    position: absolute; left: 69px; top: 24px; width: 244px; height: 20px;
    border: none; background: #fff; border-radius: 2px;
  }
  .signup-action {
    position: absolute; left: 69px; top: 44px; font-size: 26px; font-weight: 500;
    display: flex; align-items: center; gap: 10px;
  }
  .video-link {
    position: absolute; left: 517px; top: 556px; display: flex; align-items: center; gap: 8px;
    font-size: 12px; color: var(--text-grey);
  }
  .footer {
    position: absolute; left: 0; top: 601px; width: 1200px; height: 62px; background: var(--footer-bg);
  }
  .footer-nav {
    position: absolute; left: 113px; top: 31px; font-size: 11px; color: var(--text-dark);
    white-space: nowrap;
  }
  .footer-nav .bar { margin: 0 4px; color: #888; }
  .pricing { position: relative; text-decoration: line-through; text-decoration-color: var(--pricing-red); }
  .pricing-note {
    position: absolute; left: -16px; top: -17px; font-size: 9px; color: var(--pricing-red);
    white-space: nowrap; transform: rotate(-4deg);
  }
  .social { position: absolute; left: 990px; top: 18px; display: flex; gap: 14px; }
  .social-item { display: flex; align-items: center; gap: 4px; font-size: 10px; color: var(--text-dark); }
  .social-item span.square { width: 12px; height: 12px; background: var(--brand-blue); }
</style>
</head>
<body>
  <div class="column"></div>

  <div class="brand"><span class="brand-dot"></span><span class="brand-name">Pondly.io</span></div>
  <div class="access-button">Access your shares</div>

  <div class="share-now">Share NOW!</div>
  <div class="feature-tab tab-fastest">Certified fastest sharing in the market</div>
  <div class="feature-tab tab-social">Its social!</div>

  <h1 class="tagline">Drag information, add people, BOOM!</h1>
  <p class="categories">
    <span style="color:var(--c-files)">FILES</span><span class="sep">•</span>
    <span style="color:var(--c-pictures)">PICTURES</span><span class="sep">•</span>
    <span style="color:var(--c-tasks)">TASKS</span><span class="sep">•</span>
    <span style="color:var(--c-todos)">TO-DOS</span><span class="sep">•</span>
    <span style="color:var(--c-calendars)">CALENDARS</span><span class="sep">•</span>
    <span style="color:var(--c-notes)">NOTES</span><span class="sep">•</span>
    <span style="color:var(--c-links)">LINKS</span>
  </p>

  <div class="drop-zone">
    <svg width="46" height="46" viewBox="0 0 46 46" aria-hidden="true">
      <rect x="17" y="0" width="12" height="46" fill="var(--drop-plus)"/>
      <rect x="0" y="17" width="46" height="12" fill="var(--drop-plus)"/>
    </svg>
    <span>Drag files here to<br>share immediately</span>
  </div>

  <div class="or-label">OR</div>

  <div class="signup">
    <svg class="envelope" width="46" height="34" viewBox="0 0 46 34" aria-hidden="true">
      <rect x="0" y="0" width="46" height="34" fill="#fff"/>
      <polyline points="2,2 23,20 44,2" fill="none" stroke="var(--signup-purple)" stroke-width="2.5"/>
    </svg>
    <span class="signup-label">Enter business email</span>
    <input class="signup-input" type="email" aria-label="Business email">
    <div class="signup-action">Start Sharing
      <svg width="36" height="20" viewBox="0 0 36 20" aria-hidden="true">
        <polygon points="0,0 11,10 0,20" fill="var(--signup-arrow)"/>
        <polygon points="12,0 23,10 12,20" fill="var(--signup-arrow)"/>
        <polygon points="24,0 35,10 24,20" fill="var(--signup-arrow)"/>
      </svg>
    </div>
  </div>

  <div class="video-link">What is it? Watch Video
    <svg width="33" height="33" viewBox="0 0 33 33" aria-hidden="true">
      <rect x="0" y="0" width="33" height="33" rx="3" fill="#5aa9dc"/>
      <rect x="6" y="9" width="21" height="17" fill="#fff"/>
      <polygon points="13,12 21,17.5 13,23" fill="#5aa9dc"/>
      <polyline points="12,4 16.5,9 21,4" fill="none" stroke="#fff" stroke-width="1.5"/>
    </svg>
  </div>

  <footer class="footer">
    <nav class="footer-nav">
      Home<span class="bar">|</span>About Us<span class="bar">|</span>Product Tour<span class="bar">|</span><span class="pricing"><span class="pricing-note">FREE! for unlimited users.</span>Pricing</span><span class="bar">|</span>Terms Of Use<span class="bar">|</span>Jobs<span class="bar">|</span>Sign Up<span class="bar">|</span>Blog<span class="bar">|</span>Press<span class="bar">|</span>Contact Us
    </nav>
    <div class="social">
      <span class="social-item"><span class="square"></span>Chirpline</span>
      <span class="social-item"><span class="square"></span>Friendbook</span>
      <span class="social-item"><span class="square"></span>Circlenet</span>
    </div>
  </footer>
</body>
</html>
```